Steady Harbor Leadership Roundtable Series Promotion

I'm wanting a single page (for now) website to promote my leadership training. Content would include: basic messaging what Steady Harbor means, invitation to join the Steady Harbor Roundtable workshops, have me come speak to them, join me on a leadership getaway, get personal coaching, watch some video links of Rud, then referrals of people saying nice things about Rud, connect to Rud’s personal website to learn more about me. The goal of the page is to 1) get people excited to attend a workshop, hear me speak, coach them, or join me on a getaway trip, 2) educate them in how they can get in control of their own life, and 3) link to my personal site to learn more about me. This is the general idea: https://www.perlwickstand.com/

Target Market(s)

Business owners or self improvement enthusiasts looking to take their businesses and personal lives to the next level.

Industry/Entity Type

Business Consultant

Coding

Coded - Design and coding required

Number of Pages Required

1 page

Font styles to use
Other font styles liked:
• See uploaded logo

Colors
0392cd

Requirements
Must have
• Fonts and colors that match the logo that was uploaded. Uplifting, inspirational look and feel.
Nice to have
• Similar to: https://www.perlwickstand.com/ and https://dorvankessling.com/

```html
<!DOCTYPE html>
<html lang="en">
<head>
<meta charset="utf-8">
<title>Steady Harbor Roundtable</title>
<link href="https://fonts.googleapis.com/css2?family=Poppins:wght@300;400;500;600&family=Lora:ital@1&display=swap" rel="stylesheet">
<style>
:root{
  --purple:#4a2c92;
  --purple-deep:#3d2380;
  --ink:#3b2a7c;
  --cyan:#38b6ec;
  --cyan-soft:#7fd0f3;
  --orange:#f15a22;
  --grey:#6d6d7a;
  --line:#e4e6ee;
  --white:#fff;
}
*{box-sizing:border-box;margin:0;padding:0}
html,body{width:1200px;height:4351px;overflow:hidden;background:var(--white)}
body{font-family:'Poppins',sans-serif;color:var(--grey);position:relative}
.abs{position:absolute}
a{color:inherit;text-decoration:none}

/* header */
.site-header{left:0;top:0;width:1200px;height:120px;background:var(--purple);color:#fff}
.site-header .phone{left:206px;top:20px;font-size:12px;color:var(--cyan);display:flex;align-items:center;gap:6px}
.site-header .rule{height:1px;background:rgba(255,255,255,.25);top:47px}
.site-header .cta{left:887px;top:20px;font-size:12px;color:var(--cyan)}
.nav-link{top:75px;font-size:12.5px;color:#fff}
.nav-link.active{color:var(--cyan)}
.brand{left:500px;top:50px;width:200px;text-align:center;font-size:24px;font-weight:500;letter-spacing:3px;color:#fff}

/* hero */
.hero{left:0;top:120px;width:1200px;height:561px;background:linear-gradient(90deg,#f5f7f8 0%,#eef2f3 40%,#c8d2d6 70%,#8e9ca6 100%)}
.hero-photo{left:430px;top:120px;width:770px;height:561px;background:linear-gradient(90deg,rgba(245,247,248,0) 0%,rgba(200,210,216,.6) 45%,rgba(70,70,80,.55) 75%,rgba(150,160,170,.5) 100%)}
.hero h1{left:80px;top:328px;font-size:42px;font-weight:300;line-height:48px;color:var(--ink)}
.btn{display:flex;align-items:center;justify-content:center;border:2px solid var(--cyan);border-radius:20px;font-size:11.5px;color:var(--ink);background:#fff}
.hero .btn{left:81px;top:456px;width:127px;height:39px}

/* welcome */
.welcome{left:0;top:681px;width:1200px;height:870px;background:linear-gradient(180deg,#fff 0%,#f1f4f6 100%)}
.eyebrow{font-size:14px;color:var(--cyan);width:1200px;text-align:center;left:0}
.section-title{font-size:31px;font-weight:300;color:var(--ink);width:1200px;text-align:center;left:0}
.spaced{font-size:18px;font-weight:600;letter-spacing:5px;color:var(--ink);width:1200px;text-align:center;left:0}
.welcome-art{left:127px;top:879px;width:431px;height:405px;border-radius:8px;background:linear-gradient(135deg,rgba(127,208,243,.35) 0%,rgba(56,182,236,.15) 50%,rgba(90,100,120,.12) 100%)}
.welcome-copy{left:639px;width:362px}
.welcome-copy h3{font-size:16px;font-weight:400;line-height:24px;color:var(--ink)}
.welcome-copy p{font-size:11px;line-height:17.5px;text-align:justify}

/* services */
.testimonial{left:0;top:1551px;width:1200px;height:800px;background:radial-gradient(ellipse at 50% 40%,#5a5350 0%,#3d3a3b 55%,#262425 100%)}
.diamond{width:283px;height:283px;transform:rotate(45deg);transform-origin:center}
.diamond.purple{background:linear-gradient(135deg,#5a38b0,#3c2384)}
.diamond.orange{background:linear-gradient(135deg,#f36a2a,#b8380f)}
.svc{width:300px;text-align:center;color:#fff}
.svc .name{font-size:29px;font-weight:300;line-height:34px}
.svc .sub{font-size:19px;font-weight:600;line-height:24px}
.circle-arrow{width:38px;height:38px;border:1.5px solid #fff;border-radius:50%;display:flex;align-items:center;justify-content:center}
.more{width:78px;height:36px;border-radius:18px;background:var(--cyan);color:#fff;font-size:11.5px;display:flex;align-items:center;justify-content:center}

.quote-title{left:0;width:1200px;text-align:center;color:#fff;font-size:29px;font-weight:300}
.quote-body{left:270px;width:660px;text-align:center;color:#fff;font-family:'Lora',serif;font-style:italic;font-size:15px;line-height:29px}
.person{left:482px;top:2103px;display:flex;align-items:center;gap:12px;color:#fff}
.avatar{width:60px;height:60px;border-radius:50%;background:linear-gradient(135deg,#b7b2ad,#6d6762)}
.person .who{font-size:14px;font-weight:500}
.person .role{font-size:11px;line-height:17px}
.chev{color:#fff;font-size:20px}

/* workshops */
.card{width:361px;height:446px;background:#fff;box-shadow:0 4px 18px rgba(40,40,80,.1)}
.card .photo{height:199px;position:relative}
.card .date{position:absolute;left:32px;bottom:12px;font-size:10px;color:#fff;font-weight:500;letter-spacing:.5px}
.card h4{margin:28px 32px 0;font-size:19px;font-weight:400;line-height:27px;color:var(--ink)}
.card .bar{margin:8px 32px 0;width:38px;height:2px;background:var(--cyan)}
.card p{margin:16px 32px 0;font-size:11px;line-height:19px}
.card .btn{position:absolute;left:34px;bottom:31px;width:113px;height:38px}
.grey-chev{color:#8b8b96;font-size:20px}

/* videos */
.videos{left:0;top:2932px;width:1200px;height:625px;background:var(--purple)}
.thumb{width:321px;height:200px;top:3101px;background:linear-gradient(135deg,#b98e6a 0%,#d9b58e 40%,#8c6a55 100%);display:flex;align-items:center;justify-content:center}
.play{width:38px;height:38px;border:3px solid #fff;border-radius:50%;display:flex;align-items:center;justify-content:center}
.caption{width:321px;top:3325px;text-align:center;color:#fff;font-size:14px;line-height:22px}

/* contact */
.contact-bg{left:0;top:3436px;width:1200px;height:530px;background:linear-gradient(180deg,#f7f8fb,#eef0f4)}
.field{border:1px solid var(--line);border-radius:18px;background:rgba(255,255,255,.85);font-size:11px;color:#a6a8b6;padding:11px 18px}
.submit{left:544px;top:3857px;width:112px;height:39px;border-radius:20px;background:var(--cyan);color:#fff;font-size:12px;display:flex;align-items:center;justify-content:center}

/* footer */
.footer{left:0;top:3966px;width:1200px;height:385px;background:var(--purple);color:#fff}
.footer h5{font-size:14px;font-weight:600}
.footer .links{font-size:10.5px;line-height:24px}
.social{width:30px;height:30px;border:1px solid #fff;border-radius:50%}
.footer .divider{left:0;top:4276px;width:1200px;height:1px;background:rgba(255,255,255,.15)}
.copy{left:199px;top:4300px;font-size:10px;line-height:16px;color:var(--cyan)}
.subscribe{left:480px;top:4293px;width:520px;height:38px;border:1px solid var(--cyan);border-radius:20px;display:flex;align-items:center;padding-left:24px;font-size:12px;color:var(--cyan)}
.subscribe .go{position:absolute;right:-1px;top:-1px;width:240px;height:38px;border-radius:20px;background:var(--cyan);color:#fff;display:flex;align-items:center;justify-content:center}
</style>
</head>
<body>

<!-- Header -->
<header class="site-header abs">
  <div class="phone abs">
    <svg width="11" height="11" viewBox="0 0 24 24"><path fill="#38b6ec" d="M6.6 10.8a15.2 15.2 0 006.6 6.6l2.2-2.2c.3-.3.7-.4 1-.2 1.1.4 2.3.6 3.6.6.6 0 1 .4 1 1V20c0 .6-.4 1-1 1A17 17 0 013 4c0-.6.4-1 1-1h3.5c.6 0 1 .4 1 1 0 1.3.2 2.5.6 3.6.1.3 0 .7-.2 1z"/></svg>
    555-0142-7788
  </div>
  <div class="rule abs" style="left:164px;width:194px"></div>
  <div class="cta abs">Get Started Now!</div>
  <div class="rule abs" style="left:837px;width:203px"></div>
  <a class="nav-link active abs" style="left:79px">My Story</a>
  <a class="nav-link abs" style="left:193px">Leadership Training</a>
  <a class="nav-link abs" style="left:370px">Workshops</a>
  <div class="brand abs">STEADY HARBOR</div>
  <a class="nav-link abs" style="left:760px">Personal Coaching</a>
  <a class="nav-link abs" style="left:936px">Client Review</a>
  <a class="nav-link abs" style="left:1072px">Contact</a>
</header>

<!-- Hero -->
<section class="hero abs"></section>
<div class="hero-photo abs" role="img" aria-label="Photo of the coach seated in an office chair by a bright window"></div>
<h1 class="abs" style="left:80px;top:328px;font-size:42px;font-weight:300;line-height:48px;color:var(--ink)">Tap into your potential and<br>what you truly desire</h1>
<a class="btn abs" style="left:81px;top:456px;width:127px;height:39px">Contact Me</a>

<!-- Welcome -->
<section class="welcome abs"></section>
<div class="eyebrow abs" style="top:750px">Welcome to</div>
<div class="section-title abs" style="top:782px">Steady Harbor Roundtable</div>
<div class="spaced abs" style="top:822px">ROUNDTABLE</div>
<div class="welcome-art abs" role="img" aria-label="Large soft brand decoration in light blue and slate"></div>
<div class="welcome-copy abs" style="top:916px">
  <h3>40 years of helping others create<br>success and fulfillment</h3>
  <p style="margin-top:18px">Lorem ipsum dolor sit amet, consectetur adipiscing elit, sed do eiusmod tempor incididunt ut labore et dolore magna aliqua. Ut enim ad minim veniam, quis nostrud exercitation ullamco laboris nisi ut aliquip ex ea commodo consequat. Duis aute irure dolor in reprehenderit.</p>
  <p style="margin-top:17px">Sed ut perspiciatis unde omnis iste natus error sit voluptatem accusantium doloremque laudantium, totam rem aperiam, eaque ipsa quae ab illo inventore veritatis et quasi architecto beatae vitae dicta sunt explicabo.</p>
</div>
<a class="btn abs" style="left:639px;top:1201px;width:113px;height:39px">My Story</a>

<!-- Testimonial backdrop -->
<section class="testimonial abs" role="img" aria-label="Blurred photo of a workshop audience listening"></section>

<!-- Service diamonds -->
<div class="diamond purple abs" style="left:138px;top:1410px"></div>
<div class="diamond orange abs" style="left:459px;top:1410px"></div>
<div class="diamond purple abs" style="left:778px;top:1410px"></div>

<div class="svc abs" style="left:129px;top:1455px">
  <svg width="66" height="62" viewBox="0 0 66 62" fill="none" stroke="#38b6ec" stroke-width="2.5"><circle cx="22" cy="9" r="6"/><path d="M14 20h16v20h-4v20h-8V40h-4z"/><rect x="38" y="4" width="22" height="16"/><path d="M30 24l10-6"/></svg>
  <div class="name">Leadership</div><div class="sub">Training</div>
</div>
<div class="circle-arrow abs" style="left:260px;top:1633px"><svg width="10" height="12" viewBox="0 0 10 12"><path d="M2 1l6 5-6 5" stroke="#fff" stroke-width="2" fill="none"/></svg></div>

<div class="svc abs" style="left:450px;top:1455px">
  <svg width="66" height="62" viewBox="0 0 66 62" fill="none" stroke="#fff" stroke-width="2.5"><rect x="30" y="4" width="26" height="16" rx="2"/><circle cx="24" cy="22" r="5"/><path d="M12 34h30l-5 24H17z"/><path d="M14 40h26"/></svg>
  <div class="name">Mastermind</div><div class="sub">Workshops</div>
</div>
<div class="more abs" style="left:561px;top:1634px">More</div>

<div class="svc abs" style="left:769px;top:1455px">
  <svg width="66" height="62" viewBox="0 0 66 62" fill="none" stroke="#38b6ec" stroke-width="2.5"><rect x="20" y="2" width="26" height="18" rx="3"/><circle cx="18" cy="34" r="6"/><circle cx="48" cy="34" r="6"/><path d="M6 58c0-8 5-13 12-13s12 5 12 13M36 58c0-8 5-13 12-13s12 5 12 13"/></svg>
  <div class="name">Personal</div><div class="sub">Coaching</div>
</div>
<div class="circle-arrow abs" style="left:900px;top:1633px"><svg width="10" height="12" viewBox="0 0 10 12"><path d="M2 1l6 5-6 5" stroke="#fff" stroke-width="2" fill="none"/></svg></div>

<!-- Testimonial -->
<svg class="abs" style="left:590px;top:1822px" width="20" height="16" viewBox="0 0 20 16"><path fill="#38b6ec" d="M0 16V9C0 4 2 1 7 0l1 2C5 3 4 5 4 7h4v9zm11 0V9c0-5 2-8 7-9l1 2c-3 1-4 3-4 5h4v9z"/></svg>
<div class="quote-title abs" style="top:1855px">What our people Say</div>
<p class="quote-body abs" style="top:1918px">Lorem ipsum dolor sit amet, consectetur adipiscing elit, sed do eiusmod tempor incididunt ut labore et dolore magna aliqua. Ut enim ad minim veniam, quis nostrud exercitation ullamco laboris nisi ut aliquip ex ea commodo consequat. Duis aute irure dolor in reprehenderit in voluptate velit esse cillum dolore eu fugiat nulla pariatur ...</p>
<div class="chev abs" style="left:134px;top:1978px">&#8249;</div>
<div class="chev abs" style="left:1053px;top:1978px">&#8250;</div>
<div class="person abs">
  <div class="avatar" role="img" aria-label="Portrait of the reviewer"></div>
  <div><div class="who">Lena Marsh</div><div class="role">Human Resources Director<br>Brightline Lens Co.</div></div>
</div>

<!-- Curve into workshops -->
<svg class="abs" style="left:0;top:2225px" width="1200" height="130" viewBox="0 0 1200 130">
  <path d="M0 124 Q600 -36 1200 124 V130 H0z" fill="#fff"/>
  <path d="M0 124 Q600 -36 1200 124" stroke="#38b6ec" stroke-width="5" fill="none"/>
</svg>
<section class="abs" style="left:0;top:2349px;width:1200px;height:583px;background:#fff"></section>

<!-- Workshops -->
<div class="eyebrow abs" style="top:2309px">Workshop</div>
<div class="section-title abs" style="top:2340px">Attend a Workshop</div>
<div class="grey-chev abs" style="left:134px;top:2620px">&#8249;</div>
<div class="grey-chev abs" style="left:1053px;top:2620px">&#8250;</div>

<article class="card abs" style="left:199px;top:2410px">
  <div class="photo" role="img" aria-label="Photo of a person doing push-ups on grass at sunrise" style="background:linear-gradient(135deg,#e6b26d,#7f9a4d 60%,#4f6b36)"><span class="date">NOV 7 - 10, 2019 &nbsp;I&nbsp; MIAMI</span></div>
  <h4>Unleash the power<br>within</h4><div class="bar"></div>
  <p>Sed ut perspiciatis unde omnis iste natus error sit aque quae ab illo inventore veritatis et quasi architecto beatae vitae dicta.</p>
  <a class="btn">Book Now</a>
</article>
<article class="card abs" style="left:639px;top:2410px">
  <div class="photo" role="img" aria-label="Photo of a woman paddling a yellow kayak on a bay" style="background:linear-gradient(180deg,#a9b9c4,#5d7a86 55%,#35505a)"><span class="date">AUG 21 - 28, 2019 &nbsp;I&nbsp; SPAIN</span></div>
  <h4>Life and Wealth<br>Mastery</h4><div class="bar"></div>
  <p>Sed ut perspiciatis unde omnis iste natus error sit aque quae ab illo inventore veritatis et quasi architecto beatae vitae dicta.</p>
  <a class="btn">Book Now</a>
</article>

<!-- Videos -->
<section class="videos abs"></section>
<div class="eyebrow abs" style="top:3002px">Video</div>
<div class="section-title abs" style="top:3032px;color:#fff">Hear Me Speak</div>
<div class="thumb abs" style="left:79px" role="img" aria-label="Video still of a microphone on stage"><div class="play"><svg width="12" height="14"><path d="M2 1l9 6-9 6z" fill="#fff"/></svg></div></div>
<div class="thumb abs" style="left:439px" role="img" aria-label="Video still of a microphone on stage"><div class="play"><svg width="12" height="14"><path d="M2 1l9 6-9 6z" fill="#fff"/></svg></div></div>
<div class="thumb abs" style="left:799px" role="img" aria-label="Video still of a microphone on stage"><div class="play"><svg width="12" height="14"><path d="M2 1l9 6-9 6z" fill="#fff"/></svg></div></div>
<p class="caption abs" style="left:79px">At vero eos et accusamus et iusto<br>odio dignissimos ducimus.</p>
<p class="caption abs" style="left:439px">At vero eos et accusamus et iusto<br>odio dignissimos ducimus.</p>
<p class="caption abs" style="left:799px">At vero eos et accusamus et iusto<br>odio dignissimos ducimus.</p>

<!-- Contact -->
<section class="contact-bg abs" role="img" aria-label="Faded photo of a meeting room"></section>
<svg class="abs" style="left:0;top:3430px" width="1200" height="130" viewBox="0 0 1200 130">
  <path d="M0 0 H1200 V124 Q600 -36 0 124z" fill="#4a2c92"/>
  <path d="M0 124 Q600 -36 1200 124" stroke="#38b6ec" stroke-width="5" fill="none"/>
</svg>
<div class="eyebrow abs" style="top:3515px">Get Started</div>
<div class="section-title abs" style="top:3548px">Don't know how to start?</div>
<div class="spaced abs" style="top:3589px">CONTACT ME</div>
<div class="field abs" style="left:199px;top:3650px;width:387px;height:35px">Enter your Name</div>
<div class="field abs" style="left:199px;top:3713px;width:387px;height:35px">Email</div>
<div class="field abs" style="left:199px;top:3777px;width:387px;height:35px">Phone</div>
<div class="field abs" style="left:612px;top:3650px;width:388px;height:35px">Subject</div>
<div class="field abs" style="left:612px;top:3713px;width:388px;height:100px">Type your Message ...</div>
<a class="submit abs">Submit</a>

<!-- Footer -->
<footer class="footer abs"></footer>
<h5 class="abs" style="left:199px;top:4038px;color:#fff;font-size:14px;font-weight:600">Contact Info</h5>
<div class="abs" style="left:199px;top:4068px;color:#fff;font-size:15px">Call. 555-0142-7788</div>
<div class="abs" style="left:199px;top:4092px;color:#fff;font-size:10.5px">e.hello@steadyharbor.example</div>

<h5 class="abs" style="left:480px;top:4038px;color:#fff;font-size:14px;font-weight:600">Quick Link</h5>
<div class="abs" style="left:480px;top:4064px;color:#fff;font-size:10.5px;line-height:24px">My Story<br>Leadership Training<br>Workshops<br>Personal Coaching<br>Client Review<br>Contact</div>

<h5 class="abs" style="left:659px;top:4038px;color:#fff;font-size:14px;font-weight:600">Info</h5>
<div class="abs" style="left:659px;top:4064px;color:#fff;font-size:10.5px;line-height:24px">Privacy Policy<br>Terms<br>Site map</div>

<h5 class="abs" style="left:881px;top:4038px;color:#fff;font-size:14px;font-weight:600">Get Social</h5>
<div class="social abs" style="left:840px;top:4075px" aria-label="Social link"></div>
<div class="social abs" style="left:883px;top:4075px" aria-label="Social link"></div>
<div class="social abs" style="left:927px;top:4075px" aria-label="Social link"></div>
<div class="social abs" style="left:970px;top:4075px" aria-label="Social link"></div>

<div class="abs" style="left:0;top:4276px;width:1200px;height:1px;background:rgba(255,255,255,.15)"></div>
<div class="copy abs">&copy; 2019 Steady Harbor<br>Roundtable</div>
<div class="subscribe abs">Name@email.com<span class="go">Join me on a Getaway Trip</span></div>

</body>
</html>
```